Need new website for my business

I want to design a new Irrigation website for our business. What we are looking for is to have a residential section that describes providing for irrigation service for residential customers in homeowners Association. From startups to service to winterization in full residential installs.
A commercial section on our webpage describing. installation of commercial Irrigation systems. Service start-up of systems. To winterizations. Offering contract service plans for commercial customers.
Service for both commercial residential include making sure all zones are operating check for leaks adjust spray nozzles in rotors making sure all irrigation heads rotate, and are not stuck or damaged making sure that we have full coverage of each Irrigation zone for lawns. In all drip irrigation is Functioning in watering the plants accordingly. Adjusting control settings to make sure you have the right watering times during the hot dry months.
Have a landscape lighting tab:
Describing what landscape lighting and what it does to enhance curb, appeal, highlight architectural, features of landscape and transferring your outdoor space into inviting visual stunning areas with low-voltage landscape lighting
And a residential snow plowing for the Falmouth Maine area. In commercial snow, plowing and snow removal covering Scarborough south portland Portland Falmouth in Cumberland Maine for commercial Snow services. From plow & Salting parking lots to Snow removing, and Snow displacement.
we started a website but it needs a up lift and bring it to pop
our web site is willowbrookyards314.com
here are a few websites that we really like:
www.sprinklecoastal.com
www.dewpointwatering.com
www.verdantlawnsystems.com
Industry/Entity Type
Irrigation & Landscape Lighting
Coding
Coded - Design and coding required
Number of Pages Required
4 page

```html
<!DOCTYPE html>
<html lang="en">
<head>
<meta charset="utf-8">
<title>Willowbrook Yards — Irrigation, Lighting &amp; Snow Services</title>
<link href="https://fonts.googleapis.com/css2?family=Outfit:wght@500;600;700&family=Poppins:wght@400;500;600&display=swap" rel="stylesheet">
<style>
:root{
  --green:#1aa515;
  --green-dark:#128a10;
  --green-deep:#0b3a25;
  --mint:#e6f5e1;
  --cream:#f6f7ec;
  --blue:#1673c4;
  --ink:#1d1f1c;
  --muted:#5a5f58;
  --line:#e2e6df;
  --white:#ffffff;
}
*{box-sizing:border-box;margin:0;padding:0}
html,body{width:1200px;height:4376px;overflow:hidden}
body{position:relative;background:var(--white);font-family:"Poppins",sans-serif;color:var(--ink)}
h1,h2,h3,.brand,.stat-num{font-family:"Outfit",sans-serif}
.abs{position:absolute}
.eyebrow{font-size:9px;font-weight:500;color:var(--green);text-transform:uppercase;letter-spacing:.3px}
.btn{display:inline-flex;align-items:center;justify-content:center;font-size:9px;font-weight:600;text-transform:uppercase;color:#fff;background:var(--green);border-radius:5px;letter-spacing:.3px}
.photo{border-radius:14px}

/* header */
.site-header{top:0;left:0;width:1200px;height:95px}
.brand{position:absolute;left:125px;top:22px;font-weight:700;color:var(--green);font-size:34px;line-height:1}
.brand small{display:block;font-family:"Poppins",sans-serif;font-size:9px;font-weight:500;color:var(--green);margin-top:4px}
.nav{position:absolute;left:418px;top:41px;display:flex;gap:24px;font-size:9.5px;font-weight:600;text-transform:uppercase}
.nav .active{color:var(--green)}
.phone-btn{position:absolute;left:920px;top:30px;width:110px;height:32px;border-radius:6px;background:var(--mint);font-size:10px;font-weight:600;display:flex;align-items:center;justify-content:center;gap:6px}
.search-btn{position:absolute;left:1040px;top:30px;width:34px;height:32px;border-radius:6px;background:var(--mint);display:flex;align-items:center;justify-content:center}

/* hero */
.hero{top:95px;left:0;width:1200px;height:635px;border-radius:18px;overflow:hidden;background:linear-gradient(100deg,#19b012 0%,#1a9b3c 55%,#1676c2 100%)}
.hero h1{position:absolute;left:125px;top:42px;color:#fff;font-size:37px;line-height:43px;font-weight:700}
.hero-photo{position:absolute;left:0;top:177px;width:1200px;height:458px;background:linear-gradient(120deg,#2f5fb0 0%,#6a9a3a 25%,#8fc04a 50%,#5d8f2b 75%,#c8a13a 100%)}
.consult{position:absolute;left:736px;top:123px;width:339px;height:412px;background:var(--green);border-radius:14px;padding:26px 32px}
.consult h3{color:#fff;font-size:16px;font-weight:600;margin-bottom:14px}
.field-grid{display:grid;grid-template-columns:1fr 1fr;gap:10px 10px}
.field label{display:block;color:#fff;font-size:8px;margin-bottom:4px}
.field .box{height:33px;background:#fff;border-radius:5px}
.field.full{grid-column:1/3}
.field .tall{height:72px}
.consult .submit{margin-top:20px;width:100%;height:34px;background:var(--green-deep);border-radius:6px;color:#fff;font-size:9px;font-weight:600;display:flex;align-items:center;justify-content:center}

/* stats */
.stats{top:775px;left:270px;width:670px;height:60px;display:flex;justify-content:space-between}
.stat{display:flex;align-items:center;gap:12px;padding:0 28px}
.stat + .stat{border-left:1px solid var(--line)}
.stat-icon{width:44px;height:40px;border-radius:8px;background:var(--mint)}
.stat-num{font-size:24px;font-weight:600;line-height:1}
.stat-label{font-size:8px;text-transform:uppercase;margin-top:6px}

/* about */
.about-card{top:920px;left:178px;width:420px;height:368px;background:var(--mint);border-radius:14px;padding:56px 66px}
.about-card h2{font-size:21px;line-height:26px;margin:12px 0 16px;font-weight:600}
.about-card p{font-size:9.5px;line-height:15px;color:var(--muted);margin-bottom:10px}
.about-card .btn{width:94px;height:34px;margin-top:18px}
.about-photo{top:920px;left:609px;width:419px;height:368px;background:linear-gradient(160deg,#3c4a3e,#6d7d55 45%,#4e8a32 80%,#2e5a24)}

/* services */
.center{left:0;width:1200px;text-align:center}
.section-title{font-size:22px;font-weight:600}
.service{top:1455px;width:201px}
.service .img{height:287px;border-radius:12px}
.service h3{font-size:13px;font-weight:600;margin-top:22px}
.service p{font-size:9.5px;line-height:15px;color:var(--muted);margin-top:6px}

/* benefits */
.benefits{top:2045px;left:18px;width:1164px;height:380px;background:linear-gradient(160deg,#1db317,#16a011);border-radius:16px}
.benefit{top:2182px;width:277px;height:186px;background:var(--cream);border-radius:12px;padding:28px 38px}
.benefit .icon{width:58px;height:38px;border-radius:6px;background:#e2e8d6}
.benefit h3{font-size:12.5px;font-weight:600;margin:16px 0 10px}
.benefit p{font-size:9.5px;line-height:15px;color:var(--muted)}

/* plans */
.plans{top:2515px;left:250px;width:420px}
.plans h2{font-size:21px;font-weight:600;margin:6px 0 12px}
.plans p{font-size:9.5px;line-height:15px;color:var(--muted)}
.plans .btn{width:150px;height:35px;margin-top:16px;background:linear-gradient(90deg,var(--green),var(--blue))}
.plan-list{top:2528px;left:700px;width:252px;list-style:none}
.plan-list li{display:flex;align-items:center;gap:10px;height:35px;font-size:9.5px;color:var(--muted);border-bottom:1px solid var(--line)}
.plan-list li:last-child{border-bottom:none}

/* feature */
.feature-photo{top:2750px;left:178px;width:846px;height:437px;background:linear-gradient(150deg,#21341f,#3e5a2c 40%,#7b7a62 65%,#2f3b2c)}
.feature-card{top:2972px;left:728px;width:264px;height:188px;background:var(--green);border-radius:14px;padding:36px 26px}
.feature-card h2{color:#fff;font-size:19px;line-height:22px;font-weight:600}
.feature-card .btn{background:#fff;color:var(--ink);width:150px;height:34px;margin-top:18px}

/* areas */
.area{top:3360px;width:182px}
.area .img{height:220px;clip-path:polygon(0 28%,50% 0,100% 28%,100% 100%,0 100%)}
.area h3{font-size:13px;font-weight:600;text-align:center;margin-top:20px;line-height:17px}

/* cta */
.cta-brand{top:3715px;left:180px;color:var(--green);font-family:"Outfit",sans-serif;font-size:62px;font-weight:700;line-height:1}
.cta-brand span{display:block;font-family:"Poppins",sans-serif;font-size:18px;font-weight:500;margin-top:10px}
.cta{top:3706px;left:722px;width:330px}
.cta h2{font-size:22px;font-weight:600;margin:6px 0 10px}
.cta p{font-size:9.5px;line-height:15px;color:var(--muted)}
.cta .btn{width:172px;height:34px;margin-top:24px}

/* footer */
.site-footer{top:3985px;left:18px;width:1164px;height:391px;background:var(--green-deep);border-radius:18px 18px 0 0;color:#fff}
.f-col{position:absolute;top:95px}
.f-col h4{font-family:"Outfit",sans-serif;font-size:14px;font-weight:600;margin-bottom:14px}
.f-col p,.f-col li{font-size:8.5px;line-height:15px;list-style:none;color:#dfe9e2}
.f-input{margin-top:16px;width:250px;height:34px;background:#fff;border-radius:5px;color:#9aa;font-size:8px;display:flex;align-items:center;padding-left:12px}
.f-sub{margin-top:10px;width:250px;height:34px;border-radius:5px;background:linear-gradient(90deg,var(--green),var(--blue));font-size:8px;font-weight:600;display:flex;align-items:center;justify-content:center}
.contact-row{display:flex;gap:8px;margin-bottom:6px}
.socials{display:flex;gap:8px;margin-top:14px}
.socials span{width:22px;height:22px;border-radius:50%;border:1px solid #5f7f6d}
.copyright{position:absolute;left:0;width:1164px;bottom:42px;text-align:center;font-size:8.5px;color:#dfe9e2}
.chat{position:absolute;right:34px;bottom:62px;width:42px;height:42px;border-radius:50%;background:var(--green);display:flex;align-items:center;justify-content:center}
</style>
</head>
<body>

<header class="site-header abs">
  <div class="brand">Willowbrook Yards<small>Landscape, Lighting &amp; Irrigation</small></div>
  <nav class="nav">
    <span class="active">Home</span><span>Our Services ▾</span><span>Service Plans</span><span>About Us</span><span>Service Areas ▾</span><span>Contact Us</span>
  </nav>
  <div class="phone-btn">
    <svg width="10" height="10" viewBox="0 0 24 24"><path fill="#1d1f1c" d="M6.6 10.8a15 15 0 006.6 6.6l2.2-2.2a1 1 0 011-.25 11 11 0 003.6.6 1 1 0 011 1V20a1 1 0 01-1 1A17 17 0 013 4a1 1 0 011-1h3.5a1 1 0 011 1c0 1.25.2 2.45.6 3.6a1 1 0 01-.25 1z"/></svg>
    (207) 555-0148
  </div>
  <div class="search-btn"><svg width="10" height="10" viewBox="0 0 24 24" fill="none" stroke="#1d1f1c" stroke-width="3"><circle cx="10" cy="10" r="7"/><path d="M15 15l6 6"/></svg></div>
</header>

<section class="hero abs">
  <h1>Healthy Lawns. Smart Irrigation.<br>Year-Round Outdoor Solutions.</h1>
  <div class="hero-photo" role="img" aria-label="Landscaper kneeling on a green lawn adjusting a sprinkler head"></div>
  <form class="consult">
    <h3>Book a Free Consultation</h3>
    <div class="field-grid">
      <div class="field"><label>Name</label><div class="box"></div></div>
      <div class="field"><label>Address</label><div class="box"></div></div>
      <div class="field"><label>Phone</label><div class="box"></div></div>
      <div class="field"><label>Service</label><div class="box"></div></div>
      <div class="field full"><label>Attach File</label><div class="box"></div></div>
      <div class="field full"><label>Message</label><div class="box tall"></div></div>
    </div>
    <div class="submit">SUBMIT</div>
  </form>
</section>

<section class="stats abs">
  <div class="stat"><div class="stat-icon"></div><div><div class="stat-num">10,000+</div><div class="stat-label">Satisfied Clients</div></div></div>
  <div class="stat"><div class="stat-icon"></div><div><div class="stat-num">25+</div><div class="stat-label">Years in Business</div></div></div>
  <div class="stat"><div class="stat-icon"></div><div><div class="stat-num">120+</div><div class="stat-label">Highly Trained Staff</div></div></div>
</section>

<section class="about-card abs">
  <div class="eyebrow">From Concept to Completion</div>
  <h2>Creating and Caring for<br>Remarkable Outdoor Spaces</h2>
  <p>Willowbrook Yards Landscape &amp; Irrigation is a Maine-based company dedicated to creating healthy landscapes through smart irrigation, professional lighting, and dependable seasonal services.</p>
  <p>Our focus is quality workmanship, efficient systems, and long-term client relationships.</p>
  <span class="btn">About Us</span>
</section>
<div class="about-photo photo abs" role="img" aria-label="Stone house with a curved paver walkway and trimmed shrubs"></div>

<div class="abs center" style="top:1378px"><div class="eyebrow">Our Core Services</div></div>
<h2 class="abs center section-title" style="top:1396px">Landscaping Services that Make an Impact</h2>

<article class="service abs" style="left:178px"><div class="img" role="img" aria-label="Sprinklers watering a residential flower bed" style="background:linear-gradient(160deg,#6b5a45,#6f8a3c 55%,#c8a0b4)"></div><h3>Residential Irrigation</h3><p>Custom irrigation systems for HOA communities and homeowners...</p></article>
<article class="service abs" style="left:393px"><div class="img" role="img" aria-label="Sprinklers spraying a commercial lawn" style="background:linear-gradient(160deg,#9cc0d8,#cfe0e6 40%,#5f9a35 75%,#3d7a22)"></div><h3>Commercial Irrigation</h3><p>Large-scale irrigation systems designed for durability...</p></article>
<article class="service abs" style="left:608px"><div class="img" role="img" aria-label="Lit stone steps leading to a house at dusk" style="background:linear-gradient(170deg,#1e2a3b,#3b4452 50%,#6a5a3a 80%,#2a2e2f)"></div><h3>Landscape Lighting</h3><p>Low-voltage lighting that enhances curb appeal, safety, and...</p></article>
<article class="service abs" style="left:823px"><div class="img" role="img" aria-label="Snow plow truck clearing snow" style="background:linear-gradient(160deg,#dfe8f0,#f4f7fa 45%,#c96a3a 70%,#e8eef3)"></div><h3>Snow Plowing &amp; Removal</h3><p>Residential and commercial snow services you can rely on all...</p></article>

<div class="abs" style="top:1862px;left:525px"><span class="btn" style="width:150px;height:34px">Explore Our Services</span></div>

<section class="benefits abs"></section>
<div class="abs center" style="top:2110px;color:#fff;font-size:8px;text-transform:uppercase">Benefits</div>
<h2 class="abs center section-title" style="top:2127px;color:#fff">Benefits of Professional Landscape</h2>
<article class="benefit abs" style="left:178px"><div class="icon"></div><h3>V</h3><p>Lorem ipsum. Proin gravida nibh vel velit auctor aliquet. Aenean sollicitudin, lorem quis bibendum auctor nisi...</p></article>
<article class="benefit abs" style="left:462px"><div class="icon"></div><h3>Functional Outdoor Spaces</h3><p>Lorem ipsum. Proin gravida nibh vel velit auctor aliquet. Aenean sollicitudin, lorem quis bibendum auctor nisi...</p></article>
<article class="benefit abs" style="left:747px"><div class="icon"></div><h3>Increased Property Value</h3><p>Lorem ipsum. Proin gravida nibh vel velit auctor aliquet. Aenean sollicitudin, lorem quis bibendum auctor nisi...</p></article>

<section class="plans abs">
  <div class="eyebrow">Service Plans</div>
  <h2>Seasonal &amp; Contract Service Plans</h2>
  <p>Take the worry out of outdoor maintenance with our flexible service plans. Whether it's residential or commercial irrigation, landscape lighting, or snow management, our scheduled plans ensure your systems are professionally maintained year-round. Enjoy priority scheduling, seasonal inspections...</p>
  <span class="btn">View Service Plans</span>
</section>
<ul class="plan-list abs">
  <li><svg width="20" height="20" viewBox="0 0 20 20"><circle cx="10" cy="10" r="10" fill="#1aa515"/><path d="M6 10l3 3 5-6" stroke="#fff" stroke-width="2" fill="none"/></svg>Residential irrigation maintenance plans</li>
  <li><svg width="20" height="20" viewBox="0 0 20 20"><circle cx="10" cy="10" r="10" fill="#1aa515"/><path d="M6 10l3 3 5-6" stroke="#fff" stroke-width="2" fill="none"/></svg>Commercial irrigation service contracts</li>
  <li><svg width="20" height="20" viewBox="0 0 20 20"><circle cx="10" cy="10" r="10" fill="#1aa515"/><path d="M6 10l3 3 5-6" stroke="#fff" stroke-width="2" fill="none"/></svg>Priority scheduling</li>
  <li><svg width="20" height="20" viewBox="0 0 20 20"><circle cx="10" cy="10" r="10" fill="#1aa515"/><path d="M6 10l3 3 5-6" stroke="#fff" stroke-width="2" fill="none"/></svg>Seasonal inspections and adjustments</li>
</ul>

<div class="feature-photo photo abs" role="img" aria-label="Landscaped backyard with lit stone steps and trees at dusk"></div>
<section class="feature-card abs">
  <h2>Customized Landscape Solutions to Meet Your Unique Needs</h2>
  <span class="btn">Book a Consultation</span>
</section>

<div class="abs center" style="top:3290px"><div class="eyebrow">Service Areas</div></div>
<h2 class="abs center section-title" style="top:3308px">Proudly Serving Southern Maine</h2>
<div class="area abs" style="left:18px"><div class="img" role="img" aria-label="Coastal path in Falmouth" style="background:linear-gradient(170deg,#cfe0f0,#6f9cc0 45%,#6f8a4a 75%,#4b6a32)"></div><h3>Falmouth</h3></div>
<div class="area abs" style="left:215px"><div class="img" role="img" aria-label="Portland waterfront skyline" style="background:linear-gradient(170deg,#c7d8ea,#5b7f9c 45%,#3c5a6a 70%,#45623a)"></div><h3>Portland</h3></div>
<div class="area abs" style="left:412px"><div class="img" role="img" aria-label="Lighthouse on the South Portland shore" style="background:linear-gradient(170deg,#bcd4ee,#e5eef6 45%,#4f7ea6 70%,#6f9a3f)"></div><h3>South Portland</h3></div>
<div class="area abs" style="left:608px"><div class="img" role="img" aria-label="Aerial view of Scarborough homes" style="background:linear-gradient(170deg,#b9c9d6,#7e8f86 40%,#3e5d32 75%,#2f4a26)"></div><h3>Scarborough</h3></div>
<div class="area abs" style="left:805px"><div class="img" role="img" aria-label="Church steeple in Cumberland" style="background:linear-gradient(170deg,#cadff2,#9aa7b0 40%,#8a7a5c 70%,#4f6a35)"></div><h3>Cumberland</h3></div>
<div class="area abs" style="left:1002px"><div class="img" role="img" aria-label="Aerial view of surrounding communities" style="background:linear-gradient(170deg,#d6e4ee,#8aa4ab 35%,#4f6f3a 70%,#3a5a2a)"></div><h3>Surrounding<br>Communities</h3></div>

<div class="cta-brand abs">Willowbrook<span>Landscape, Lighting &amp; Irrigation</span></div>
<section class="cta abs">
  <div class="eyebrow">Contact Us</div>
  <h2>Let's Get Started</h2>
  <p>Whether you need irrigation installation, seasonal maintenance, lighting design, or snow services — we're here to help.</p>
  <span class="btn">Request a Free Estimate</span>
</section>

<footer class="site-footer abs">
  <div class="f-col" style="left:169px">
    <h4>Subscribe Newsletter</h4>
    <p>Subscribe to the Willowbrook Yards Landscape &amp; Irrigation<br>newsletter for the latest tips, seasonal.</p>
    <div class="f-input">✉&nbsp; Enter email address</div>
    <div class="f-sub">SUBMIT</div>
  </div>
  <div class="f-col" style="left:492px">
    <h4>Usefull Links</h4>
    <ul><li>Home</li><li>Services</li><li>Service Areas</li><li>About Us</li><li>Contact Us</li></ul>
  </div>
  <div class="f-col" style="left:637px">
    <h4>Our Services</h4>
    <ul><li>New irrigation system installation</li><li>Seasonal system startups</li><li>Complete winterization services</li><li>Full residential system installs</li></ul>
  </div>
  <div class="f-col" style="left:834px;width:190px">
    <h4>Contact Us</h4>
    <div class="contact-row"><svg width="8" height="10" viewBox="0 0 24 30"><path fill="#1aa515" d="M12 0a12 12 0 00-12 12c0 9 12 18 12 18s12-9 12-18A12 12 0 0012 0zm0 16a4 4 0 110-8 4 4 0 010 8z"/></svg><p>Visit our office 18 Meadow Lane,<br>Falmouth, Maine</p></div>
    <div class="contact-row"><svg width="9" height="9" viewBox="0 0 24 24"><path fill="#1aa515" d="M6.6 10.8a15 15 0 006.6 6.6l2.2-2.2a1 1 0 011-.25 11 11 0 003.6.6 1 1 0 011 1V20a1 1 0 01-1 1A17 17 0 013 4a1 1 0 011-1h3.5a1 1 0 011 1c0 1.25.2 2.45.6 3.6a1 1 0 01-.25 1z"/></svg><p>(207) 555-0148</p></div>
    <div class="contact-row"><svg width="9" height="9" viewBox="0 0 24 24"><rect x="2" y="5" width="20" height="14" rx="2" fill="#1aa515"/></svg><p>hello@willowbrookyards314.com</p></div>
    <div class="socials"><span></span><span></span><span></span><span></span></div>
  </div>
  <div class="copyright">Copyright © 2026 Willowbrook Yards Landscape and Property Maintenance - All Rights Reserved.</div>
  <div class="chat"><svg width="20" height="18" viewBox="0 0 24 22"><path fill="#fff" d="M2 3a3 3 0 013-3h14a3 3 0 013 3v10a3 3 0 01-3 3H9l-5 5v-5H5a3 3 0 01-3-3z"/></svg></div>
</footer>

</body>
</html>
```